Business Card - connecting 2 souls and beggining the journey of self discovery

Logo on the front
with tag line

On the back list of services and contact details

Seminars
workshops
Coaching
podcasts

Daniel Porthwick
Health & Wellbeing Life Coach
0491 372 815
daniel@wovenpathwellness.example
wovenpathwellness.example

Industry/Entity Type

Life Coaching

Contact Information for Business Card

I like the use of colour from the logo to be used. I'm not a fan of white.

Requirements
Must have
• My tagline: The journey home starts with you
Nice to have
• Use of colour that is in the mind body soul logo

```html
<!DOCTYPE html>
<html lang="en">
<head>
<meta charset="utf-8">
<title>Woven Path Wellness – Business Card</title>
<link rel="stylesheet" href="https://fonts.googleapis.com/css2?family=Open+Sans:wght@400;600&family=Oswald:wght@500&display=swap">
<style>
  :root {
    --backdrop: #e9e6e2;
    --card: #ffffff;
    --ink: #6f6f6f;
    --ink-dark: #555555;
    --purple: #8b4fb0;
    --pink: #f0596e;
    --orange: #f4a23a;
    --green: #8cc84b;
    --teal: #3fb49b;
    --mark: #f08a5d;
  }
  * { margin: 0; padding: 0; box-sizing: border-box; }
  html, body { width: 1200px; height: 1000px; overflow: hidden; }
  body {
    background: var(--backdrop);
    position: relative;
    font-family: "Open Sans", Arial, sans-serif;
    color: var(--ink);
  }
  .card {
    position: absolute;
    left: 266px;
    width: 666px;
    height: 397px;
    background: var(--card);
    border-radius: 24px;
    overflow: hidden;
    box-shadow: 0 4px 14px rgba(0,0,0,0.18);
  }
  .card--front { top: 74px; }
  .card--back { top: 533px; }

  .brand-dot {
    position: absolute;
    left: 50%;
    transform: translateX(-50%);
    border-radius: 50%;
    background: var(--mark);
  }
  .card--front .brand-dot { top: 40px; width: 116px; height: 116px; }
  .card--back .brand-dot { top: 87px; width: 136px; height: 136px; }

  .brand-name {
    position: absolute;
    left: 0; right: 0;
    text-align: center;
    font-weight: 400;
    color: var(--ink);
    letter-spacing: -0.5px;
  }
  .card--front .brand-name { top: 170px; font-size: 30px; }
  .card--back .brand-name { top: 240px; font-size: 36px; }

  .person {
    position: absolute;
    right: 352px;
    top: 241px;
    text-align: right;
  }
  .person__name {
    font-family: "Oswald", "Arial Narrow", sans-serif;
    font-weight: 500;
    font-size: 25px;
    line-height: 32px;
    color: var(--ink-dark);
    text-transform: uppercase;
  }
  .person__role { font-size: 16px; line-height: 26px; color: var(--ink); }

  .divider {
    position: absolute;
    left: 332px;
    top: 242px;
    width: 2px;
    height: 58px;
    background: var(--ink-dark);
  }

  .contact {
    position: absolute;
    left: 348px;
    top: 236px;
    list-style: none;
    font-size: 16px;
    line-height: 23.5px;
    color: var(--ink);
  }
  .contact li { display: flex; align-items: center; gap: 7px; white-space: nowrap; }
  .contact svg { width: 14px; height: 14px; fill: var(--ink-dark); flex: none; }

  .services {
    position: absolute;
    left: 0; right: 0;
    top: 324px;
    text-align: center;
    font-size: 16.5px;
    letter-spacing: 0.8px;
    color: var(--ink-dark);
    word-spacing: 2px;
  }

  .colour-band {
    position: absolute;
    left: 0; bottom: 0;
    width: 100%;
    height: 33px;
    background: linear-gradient(90deg, var(--purple), var(--pink) 35%, var(--orange) 60%, var(--green) 80%, var(--teal));
  }

  .tagline {
    position: absolute;
    left: 0; right: 0;
    top: 348px;
    text-align: center;
    font-size: 16.5px;
    letter-spacing: 0.6px;
    color: var(--ink-dark);
  }
</style>
</head>
<body>
  <section class="card card--front">
    <div class="brand-dot"></div>
    <div class="brand-name">Woven Path Wellness</div>

    <div class="person">
      <div class="person__name">Daniel Porthwick</div>
      <div class="person__role">Health &amp; Wellbeing Life Coach</div>
    </div>
    <div class="divider"></div>
    <ul class="contact">
      <li>
        <svg viewBox="0 0 16 16" aria-hidden="true"><path d="M2 6c0-2 2-3 6-3s6 1 6 3v1h-3V5.5H5V7H2zM4 8h8l2 5H2z"/></svg>
        0491 372 815
      </li>
      <li>
        <svg viewBox="0 0 16 16" aria-hidden="true"><path d="M1 3h14v10H1zm1 1v.5l6 4 6-4V4z"/></svg>
        daniel@wovenpathwellness.example
      </li>
      <li>
        <svg viewBox="0 0 16 16" aria-hidden="true"><path d="M8 1a7 7 0 1 0 0 14A7 7 0 0 0 8 1zm0 2a5 5 0 0 1 0 10A5 5 0 0 1 8 3z"/><path d="M8 4l2 4-2 4-2-4z"/></svg>
        wovenpathwellness.example
      </li>
    </ul>

    <div class="services">Seminars &nbsp;-&nbsp; Workshops &nbsp;-&nbsp; Coaching &nbsp;-&nbsp; Podcasts</div>

    <div class="colour-band"></div>
  </section>

  <section class="card card--back">
    <div class="brand-dot"></div>
    <div class="brand-name">Woven Path Wellness</div>
    <div class="tagline">The journey home starts with you</div>
  </section>
</body>
</html>
```